Trifold Pamphlet/leaflet design for Tide Nest Retreats, Trainings and Community

We would like to create a trifold leaflet showcasing Tide Nest and our retreats for promotional purposes. Tide Nest is an Australian based global company offering life-changing retreats, online trainings and inspired community within the health, wellness, personal development and human potential space.
We will use the 6 pages to showcase the Front cover with logo and tagline/keywords - Explore, Play, Connect,
Back Cover can have contact details, website , social media etc and the other 4 pages to detail
1. who Tide Nest is, what we are about, pics of the team
2. Our retreats including pictures of the Retreat Centre
3. Our Online Trainings
4 Our Inspired Community.
Each page to include text and images that I will provide shortly. Look is to align with colour palate and feel of logo and website - preview of website, in progress, here - https://kimpagecraft.sampleeditorhub.com/site/7a2c9e14/?preview=true&insitepreview=true
Little less black in the leaflets than on the website perhaps
Text is to be in poppins font.
Please advise of any questions, will forward images and text early next week - awaiting our photographer!
Best, Ned
Target Market(s)
35-55, senior leaders, business owners. 65% female, 35% male. Interested in yoga, wellbeing, peak performance, mindfulness.
Industry/Entity Type
Health And Wellness
Look and feel

```html
<!DOCTYPE html>
<html lang="en">
<head>
<meta charset="utf-8">
<title>Tide Nest Trifold Leaflet</title>
<link href="https://fonts.googleapis.com/css2?family=Poppins:ital,wght@0,300;0,400;0,500;1,400&display=swap" rel="stylesheet">
<style>
  :root {
    --backdrop: #aeadab;
    --paper: #ffffff;
    --ink: #1c1c1c;
    --ink-soft: #4a4a4a;
    --night: #050505;
    --teal: #2f8e93;
    --teal-soft: #7fb3b5;
    --teal-deep: #17808a;
    --ring: #5c9ea3;
  }
  * { box-sizing: border-box; margin: 0; padding: 0; }
  html, body { width: 1200px; height: 4000px; overflow: hidden; }
  body {
    background: var(--backdrop);
    font-family: "Poppins", sans-serif;
    color: var(--ink);
    position: relative;
  }
  .spread {
    position: absolute;
    left: 60px;
    width: 1080px;
    height: 765px;
    display: flex;
    background: var(--paper);
    overflow: hidden;
  }
  .spread--outer { top: 1135px; }
  .spread--inner { top: 2100px; }
  .panel { width: 360px; height: 100%; position: relative; padding: 40px 38px 0 34px; }

  .section-title { display: flex; align-items: flex-start; gap: 10px; margin-bottom: 20px; }
  .section-title__mark { width: 36px; height: 36px; border: 2px solid var(--ink); border-radius: 50%; flex: none; margin-top: 2px; }
  .section-title__text { font-size: 17px; font-weight: 400; line-height: 1.2; text-transform: uppercase; }
  .body-copy { font-size: 9.6px; line-height: 1.5; color: var(--ink-soft); margin-bottom: 13px; }

  .team { display: flex; justify-content: space-between; margin-top: 30px; padding: 0 2px; }
  .team__member { width: 68px; text-align: center; }
  .team__photo { width: 48px; height: 48px; border-radius: 50%; margin: 0 auto 6px; background: radial-gradient(circle at 50% 40%, #c9a78e, #5b4a40); }
  .team__name { font-size: 6.5px; font-weight: 500; }
  .team__role { font-size: 6px; color: #8a8a8a; }

  .panel--back { background: var(--night); color: #fff; text-align: center; }
  .back__ring { position: absolute; left: 70px; top: 150px; width: 220px; height: 220px; border: 5px solid #1e1e1e; border-radius: 50%; }
  .wordmark { font-weight: 300; letter-spacing: 0.06em; text-transform: uppercase; }
  .back__wordmark { position: absolute; left: 0; right: 0; top: 500px; font-size: 24px; }
  .back__contact { position: absolute; left: 0; right: 0; top: 570px; font-size: 13px; line-height: 1.45; }
  .back__contact p + p { margin-top: 14px; }

  .panel--cover { text-align: center; padding: 44px 20px 0; }
  .cover__wordmark { font-size: 38px; color: #2a2a2a; }
  .cover__photo-wrap { position: relative; width: 330px; height: 330px; margin: 26px auto 0; }
  .cover__photo-wrap svg { position: absolute; inset: 0; }
  .cover__photo { position: absolute; left: 18px; top: 18px; width: 294px; height: 294px; border-radius: 50%; background: linear-gradient(180deg, #e9e3d3 0%, #d8c49a 45%, #8c8466 75%, #5f6e49 100%); }
  .cover__headline { font-size: 28px; font-weight: 400; line-height: 1.25; text-transform: uppercase; margin-top: 44px; color: #222; }
  .cover__pill { display: inline-block; margin-top: 14px; background: var(--teal-soft); color: #fff; font-size: 14px; padding: 2px 30px; border-radius: 14px; }
  .cover__url { font-size: 9px; margin-top: 20px; }

  .rounded-photo { border-radius: 22px; }
  .retreat__photo { width: 286px; height: 400px; background: linear-gradient(180deg, #8d8c84 0%, #6b6a5f 40%, #4a4335 75%, #2e2a22 100%); margin-top: 4px; }
  .teal-heading { color: var(--teal); font-size: 17px; line-height: 1.2; font-weight: 400; margin: 28px 0 10px; }
  .teal-heading--italic em { font-style: italic; }

  .training__photo { width: 280px; height: 230px; margin: 4px auto 0; background: linear-gradient(135deg, #f2f1ec 0%, #d9dcd1 50%, #8c9a78 100%); }
  .tick-item { display: flex; gap: 8px; margin-bottom: 10px; }
  .tick-item svg { flex: none; margin-top: 1px; }
  .tick-item .body-copy { margin: 0; }

  .community__photo { width: 282px; height: 374px; margin: 34px auto 0; background: linear-gradient(180deg, #cfd6dc 0%, #8d97a0 30%, #6b6254 60%, #c4a27c 100%); }

  .footer-band { position: absolute; left: 360px; bottom: 0; width: 720px; height: 40px; }
  .footer-band__url { position: absolute; left: 410px; bottom: 12px; font-size: 9.5px; color: #fff; }
</style>
</head>
<body>

<section class="spread spread--outer">
  <article class="panel panel--about">
    <header class="section-title">
      <span class="section-title__mark"></span>
      <h2 class="section-title__text">Who<br>Tide Nest is</h2>
    </header>
    <p class="body-copy">Lorem ipsum dolor sit amet, consectetur adipiscing elit, sed do eiusmod tempor incididunt ut labore et dolore magna aliqua. Ut enim ad minim veniam, quis nostrud exercitation ullamco laboris nisi ut aliquip ex ea commodo consequat.</p>
    <p class="body-copy">Lorem ipsum dolor sit amet, consectetur adipiscing elit, sed do eiusmod tempor incididunt ut labore et dolore magna aliqua. Ut enim ad minim veniam, quis nostrud exercitation ullamco laboris nisi ut aliquip ex ea commodo consequat.</p>
    <p class="body-copy">Lorem ipsum dolor sit amet, consectetur adipiscing elit, sed do eiusmod tempor incididunt ut labore et dolore magna aliqua. Ut enim ad minim veniam, quis nostrud exercitation ullamco laboris nisi ut aliquip ex ea commodo consequat.</p>
    <header class="section-title" style="margin-top:40px">
      <span class="section-title__mark"></span>
      <h2 class="section-title__text">What<br>we are about</h2>
    </header>
    <p class="body-copy">Lorem ipsum dolor sit amet, consectetur adipiscing elit, sed do eiusmod tempor incididunt ut labore et dolore magna aliqua. Ut enim ad minim veniam, quis nostrud exercitation ullamco laboris nisi ut aliquip ex ea commodo consequat.</p>
    <p class="body-copy">Lorem ipsum dolor sit amet, consectetur adipiscing elit, sed do eiusmod tempor incididunt ut labore et dolore magna aliqua. Ut enim ad minim veniam, quis nostrud exercitation ullamco laboris nisi ut aliquip ex ea commodo consequat.</p>
    <div class="team">
      <div class="team__member"><div class="team__photo" role="img" aria-label="Portrait of team member Mara Quinlan"></div><p class="team__name">Mara Quinlan</p><p class="team__role">Founder</p></div>
      <div class="team__member"><div class="team__photo" role="img" aria-label="Portrait of team member Lena Forde"></div><p class="team__name">Lena Forde</p><p class="team__role">Coach</p></div>
      <div class="team__member"><div class="team__photo" role="img" aria-label="Portrait of team member Theo Marsh"></div><p class="team__name">Theo Marsh</p><p class="team__role">Trainer</p></div>
      <div class="team__member"><div class="team__photo" role="img" aria-label="Portrait of team member Ruby Calder"></div><p class="team__name">Ruby Calder</p><p class="team__role">Host</p></div>
    </div>
  </article>

  <article class="panel panel--back">
    <div class="back__ring"></div>
    <p class="wordmark back__wordmark">Tide Nest</p>
    <div class="back__contact">
      <p>10 Street Name, City Name<br>Country, Zip Code</p>
      <p>555 555 555</p>
      <p>example@mail.com</p>
    </div>
  </article>

  <article class="panel panel--cover">
    <p class="wordmark cover__wordmark">Tide Nest</p>
    <div class="cover__photo-wrap">
      <svg width="330" height="330" viewBox="0 0 330 330" aria-hidden="true">
        <path d="M40 250 A150 150 0 1 1 165 315" fill="none" stroke="var(--ring)" stroke-width="2.5"/>
        <path d="M28 228 A150 150 0 0 0 120 312" fill="none" stroke="var(--ring)" stroke-width="2"/>
      </svg>
      <div class="cover__photo" role="img" aria-label="Woman with arms outstretched in a sunlit misty meadow"></div>
    </div>
    <h1 class="cover__headline">Facilitating<br>flow for whole<br>human thriving</h1>
    <p class="cover__pill">Explore | Play | Connect</p>
    <p class="cover__url">www.kimpagecraft.sampleeditorhub.com</p>
  </article>
</section>

<section class="spread spread--inner">
  <article class="panel panel--retreats">
    <header class="section-title">
      <span class="section-title__mark"></span>
      <h2 class="section-title__text">Our<br>retreats</h2>
    </header>
    <div class="retreat__photo rounded-photo" role="img" aria-label="Hiker carrying a rolled yoga mat and lantern on a forest trail"></div>
    <h3 class="teal-heading">I'll guide you<br>to amazing places</h3>
    <p class="body-copy">Spend half a day exploring Banksia Ridge Park by foot. This trek is an excellent choice if you don't have time for a full-day or overnight trip. The early morning tour starts early enough to enjoy the sounds of the forest waking up. The afternoon tour finishes at dusk, so you can enjoy the quiet calm of the nighttime forest. Bring your own food and water.</p>
    <p class="body-copy">As your tour guide, I'll help you disconnect from your everyday world, so you can immerse yourself in nature and reconnect with yourself.</p>
  </article>

  <article class="panel panel--trainings">
    <header class="section-title">
      <span class="section-title__mark"></span>
      <h2 class="section-title__text">Our<br>online trainings</h2>
    </header>
    <div class="training__photo rounded-photo" role="img" aria-label="Woman working at a laptop in a bright office with plants"></div>
    <h3 class="teal-heading teal-heading--italic">Neuroscience Based Training To Help You Accomplish More, In Less Time, With <em>Greater Ease</em></h3>
    <p class="body-copy">Our peak performance training is designed to help entrepreneurs, leaders and knowledge workers perform better than ever, under any conditions.</p>
    <div class="tick-item">
      <svg width="12" height="12" viewBox="0 0 12 12" aria-hidden="true"><circle cx="6" cy="6" r="5.2" fill="none" stroke="#555" stroke-width="1"/><path d="M3.5 6.2 5.3 7.8 8.6 4.3" fill="none" stroke="#555" stroke-width="1"/></svg>
      <p class="body-copy">Lorem ipsum dolor sit amet, consectetur adipiscing elit, sed do eiusmod tempor incididunt ut labore et dolore magna aliqua. Ut enim ad minim veniam, quis nostrud exercitation ullamco laboris nisi ut aliquip ex ea commodo consequat.</p>
    </div>
    <div class="tick-item">
      <svg width="12" height="12" viewBox="0 0 12 12" aria-hidden="true"><circle cx="6" cy="6" r="5.2" fill="none" stroke="#555" stroke-width="1"/><path d="M3.5 6.2 5.3 7.8 8.6 4.3" fill="none" stroke="#555" stroke-width="1"/></svg>
      <p class="body-copy">Lorem ipsum dolor sit amet, consectetur adipiscing elit, sed do eiusmod tempor incididunt ut labore et dolore magna aliqua. Ut enim ad minim veniam, quis nostrud exercitation ullamco laboris nisi ut aliquip ex ea commodo consequat.</p>
    </div>
  </article>

  <article class="panel panel--community">
    <header class="section-title">
      <span class="section-title__mark"></span>
      <h2 class="section-title__text">Our<br>inspired community</h2>
    </header>
    <p class="body-copy">Lorem ipsum dolor sit amet, consectetur adipiscing elit, sed do eiusmod tempor incididunt ut labore et dolore magna aliqua. Ut enim ad minim veniam, quis nostrud exercitation ullamco laboris nisi ut aliquip ex ea commodo consequat.</p>
    <p class="body-copy">Lorem ipsum dolor sit amet, consectetur adipiscing elit, sed do eiusmod tempor incididunt ut labore et dolore magna aliqua. Ut enim ad minim veniam, quis nostrud exercitation ullamco laboris nisi ut aliquip ex ea commodo consequat. Lorem ipsum dolor sit amet, consectetur adipiscing elit, sed do eiusmod tempor incididunt ut labore et dolore magna aliqua. Ut enim ad minim veniam, quis nostrud exercitation ullamco laboris nisi ut aliquip ex ea commodo consequat.</p>
    <div class="community__photo rounded-photo" role="img" aria-label="Group standing arm in arm on a deck facing a mountain view"></div>
  </article>

  <svg class="footer-band" width="720" height="40" viewBox="0 0 720 40" aria-hidden="true">
    <path d="M0 40 Q60 8 200 8 L720 8 L720 40 Z" fill="var(--teal-deep)"/>
  </svg>
  <p class="footer-band__url">www.kimpagecraft.sampleeditorhub.com</p>
</section>

</body>
</html>
```